Form By Tammi - Health and Wellness Business Card and Logo

I need a business card design with a logo for my business you can check out at www.formbytammi.com. I want something more original, simplistic, and memorable than the basic logo I have on my site currently. I am a health and wellness coach and I offer mindset coaching and nutrition plans. I like the colour teal and dark grey/black for my theme colours. I emphasize growth, longterm change, and the whole package of "healthy mind, healthy body, healthy life". I had played around the idea of intertwining 3 T's or incorporating growth (leaves etc.) into my design. I want my expertise and experience to show through. In one glance I want people to understand with confidence I can help them accomplish anything they set their minds to. I look forward to seeing what everyone comes up with!

Industry/Entity Type

Health And Wellness

Contact Information for Business Card

Form By Tammi
Tammi Orlund
BSc, Health & Wellness Coach
"Manifest your best"
www.formbytammi.com
formbytammi@quillmail.com
613-472-0916
[Instagram logo] @tammiorlund

Colors
33b8a4
ffffff
333333
000000

Requirements
Must have
• A memorable and unique logo for my business!
Nice to have
• Could have the phrase "Are you unhappy with your body and state of health?" or "It takes the right skills to develop habits in order to create long term change. I can help you get there."

```html
<!DOCTYPE html>
<html lang="en">
<head>
<meta charset="utf-8">
<title>Form By Tammi – Business Card</title>
<link rel="stylesheet" href="https://fonts.googleapis.com/css2?family=Exo+2:wght@400&family=Lato:wght@400&family=Lora:ital,wght@1,400;1,700&display=swap">
<style>
  :root {
    --backdrop: #d2d2d2;
    --card-dark: #2b2b2b;
    --card-light: #ffffff;
    --teal-light: #6fcdd9;
    --teal: #2fa9a3;
    --ink: #5a5a5a;
    --ink-soft: #6a6a6a;
  }
  * { margin: 0; padding: 0; box-sizing: border-box; }
  html, body {
    width: 900px;
    height: 1200px;
    overflow: hidden;
    background: var(--backdrop);
  }
  .card {
    position: absolute;
    left: 71px;
  }
  .card--front {
    top: 129px;
    width: 756px;
    height: 442px;
    background: var(--card-dark);
    text-align: center;
  }
  .card--back {
    top: 630px;
    width: 751px;
    height: 439px;
    background: var(--card-light);
  }
  .brand-dot {
    position: absolute;
    border-radius: 50%;
  }
  .card--front .brand-dot {
    width: 56px; height: 56px;
    left: 351px; top: 150px;
    background: var(--teal-light);
  }
  .card--back .brand-dot {
    width: 56px; height: 56px;
    left: 150px; top: 90px;
    background: var(--teal);
  }
  .brand-name {
    position: absolute;
    font-family: "Exo 2", sans-serif;
    font-weight: 400;
    font-size: 40px;
    line-height: 1;
    white-space: nowrap;
  }
  .card--front .brand-name {
    left: 0; right: 0; top: 284px;
    color: var(--teal-light);
  }
  .card--back .brand-name {
    left: 60px; top: 201px;
    color: var(--teal);
  }
  .tagline {
    position: absolute;
    left: 0; right: 0; top: 358px;
    font-family: "Lora", serif;
    font-style: italic;
    font-size: 16.5px;
    line-height: 24px;
    color: var(--teal-light);
  }
  .tagline strong { font-weight: 700; }
  .contact {
    position: absolute;
    right: 51px;
    top: 292px;
    text-align: right;
    font-family: "Lato", sans-serif;
  }
  .contact__name {
    font-size: 24px;
    line-height: 30px;
    color: var(--ink);
  }
  .contact__title {
    font-size: 15px;
    line-height: 22px;
    color: var(--teal);
    margin-bottom: 5px;
  }
  .contact__line {
    font-size: 16.5px;
    line-height: 23px;
    color: var(--ink-soft);
  }
</style>
</head>
<body>
  <section class="card card--front">
    <span class="brand-dot"></span>
    <div class="brand-name">Form By Tammi</div>
    <p class="tagline">
      It takes the right skills to develop habits in order to create long term change.<br>
      <strong>I can help you get there.</strong>
    </p>
  </section>

  <section class="card card--back">
    <span class="brand-dot"></span>
    <div class="brand-name">Form By Tammi</div>
    <div class="contact">
      <p class="contact__name">Tammi Orlund</p>
      <p class="contact__title">BSc, Health &amp; Wellness Coach, Trainer</p>
      <p class="contact__line">613-472-0916 | formbytammi@quillmail.com</p>
      <p class="contact__line">www.formbytammi.com</p>
    </div>
  </section>
</body>
</html>
```